HL - business card

Harbor Lane Brokers is an insurance brokerage firm, inovative, proactive, vigorous, which aims to become the leader of the insurance brokers in Anfrica. We should like to get some designs which should be avoided also in Gray / Metallic for the Administration and Orange / Blue for the Managers (ike in the picture sent). The Blue / Green logo is not the correct one, but the source of the file. Please adjust the color accordingly for the business cards. 1 / Orange / Blue 2 / Gray / Metallic We want something classic but which is transmitted strenght, inovation, modernity and most of all, rapidity. We want something start-up like, very punchy and catching eye remaining profesional at the same time. Name: Tobias Wendell Function: Managing Director Address: N ° 17/18 Rua Dovel - R / C 2B Direita - Bairro Sambelo - Luanda Tel: (+244) 947 385 610 Email: tobias.wendell@harbor-l.com Website: www.harbor-l. com We want classic in the front and creative, colorfull at the back. The cards will be printed in relief, with very high quality of paper.
Insurance Broker
Designer to choose colors to be used in the design.

```html
<!DOCTYPE html>
<html lang="en">
<head>
<meta charset="utf-8">
<title>Harbor Lane Brokers – Business Card</title>
<link href="https://fonts.googleapis.com/css2?family=Montserrat:wght@400;500;600;700&display=swap" rel="stylesheet">
<style>
  :root {
    --page: #ececec;
    --paper: #f7f7f6;
    --charcoal: #3a3a3a;
    --ink: #555555;
    --ink-soft: #777777;
    --rule: #9a9a9a;
    --blue: #3a9bd0;
    --orange: #e89a1c;
    --silver: #d4d4d4;
    --silver-dim: #a8a8a8;
  }
  * { margin: 0; padding: 0; box-sizing: border-box; }
  html, body { width: 1200px; height: 1065px; overflow: hidden; }
  body {
    background: var(--page);
    font-family: "Montserrat", Arial, sans-serif;
    position: relative;
  }
  .card {
    position: absolute;
    width: 560px;
    height: 320px;
    overflow: hidden;
    box-shadow: 0 6px 18px rgba(0,0,0,0.12);
  }

  /* Front – manager card */
  .card--front { left: 70px; top: 560px; background: var(--paper); color: var(--ink); }
  .person { position: absolute; left: 36px; top: 36px; }
  .person__name { font-size: 22px; font-weight: 700; color: var(--ink); letter-spacing: 0.2px; }
  .person__role { font-size: 12px; font-weight: 500; color: var(--ink-soft); margin-top: 2px; }
  .rule { position: absolute; left: 36px; right: 36px; top: 98px; height: 1px; background: var(--rule); }
  .contacts { position: absolute; left: 36px; top: 112px; list-style: none; font-size: 12px; color: var(--ink-soft); line-height: 20px; }
  .contacts li { display: flex; align-items: center; gap: 8px; }
  .contacts svg { width: 12px; height: 12px; flex: none; }
  .brand { position: absolute; display: flex; align-items: center; gap: 10px; }
  .card--front .brand { right: 36px; top: 160px; }
  .brand__mark { width: 18px; height: 18px; border-radius: 50%; }
  .card--front .brand__mark { background: var(--orange); }
  .brand__name { font-weight: 600; text-transform: uppercase; letter-spacing: 1px; }
  .card--front .brand__name { font-size: 19px; color: var(--blue); }
  .address { position: absolute; right: 36px; bottom: 34px; text-align: right; font-size: 11.5px; line-height: 17px; color: var(--ink-soft); }

  /* Back – administration card */
  .card--back { left: 570px; top: 130px; background: var(--charcoal); }
  .backdrop-ring {
    position: absolute; right: -90px; top: 130px; width: 300px; height: 300px;
    border-radius: 50%; border: 34px solid rgba(255,255,255,0.04);
  }
  .card--back .brand { left: 0; right: 0; top: 118px; justify-content: center; }
  .card--back .brand__mark { width: 22px; height: 22px; border: 3px solid var(--silver); }
  .card--back .brand__name { font-size: 24px; color: var(--silver); }
  .card--back .site {
    position: absolute; left: 0; right: 0; top: 172px; text-align: center;
    font-size: 12px; font-weight: 500; letter-spacing: 1.5px; color: var(--silver-dim);
  }
</style>
</head>
<body>

  <section class="card card--back" aria-label="Business card back">
    <div class="backdrop-ring"></div>
    <div class="brand">
      <span class="brand__mark"></span>
      <span class="brand__name">Harbor Lane Brokers</span>
    </div>
    <p class="site">www.harbor-l. com</p>
  </section>

  <section class="card card--front" aria-label="Business card front">
    <div class="person">
      <h1 class="person__name">Tobias Wendell</h1>
      <p class="person__role">Managing Director</p>
    </div>
    <div class="rule"></div>
    <ul class="contacts">
      <li>
        <svg viewBox="0 0 12 12"><path d="M3 1 L5 3.5 L4 4.8 Q5 7 7.2 8 L8.5 7 L11 9 L10 11 Q4 11 1 2 Z" fill="var(--blue)"/></svg>
        (+244) 947 385 610
      </li>
      <li>
        <svg viewBox="0 0 12 12"><rect x="0.8" y="2.5" width="10.4" height="7" fill="none" stroke="var(--blue)" stroke-width="1"/><path d="M0.8 2.5 L6 6.5 L11.2 2.5" fill="none" stroke="var(--blue)" stroke-width="1"/></svg>
        tobias.wendell@harbor-l.com
      </li>
      <li>
        <svg viewBox="0 0 12 12"><circle cx="6" cy="6" r="5" fill="none" stroke="var(--blue)" stroke-width="1"/><ellipse cx="6" cy="6" rx="2.2" ry="5" fill="none" stroke="var(--blue)" stroke-width="0.9"/><path d="M1 6 H11" stroke="var(--blue)" stroke-width="0.9"/></svg>
        www.harbor-l. com
      </li>
    </ul>
    <div class="brand">
      <span class="brand__mark"></span>
      <span class="brand__name">Harbor Lane Brokers</span>
    </div>
    <address class="address" style="font-style:normal">
      N ° 17/18 Rua Dovel - R / C 2B<br>
      Direita - Bairro Sambelo - Luanda
    </address>
  </section>

</body>
</html>
```